***Rustic Website Design - More design needed after!***

Copperwick Marketing Agency
https://www.instagram.com/tallowfinchco/

Website pages:
Home
About
Design
-Logo Design and Branding
-Graphic Design
Websites
-Hosting, Maintenance and Support
Social Media
Managed Marketing
Portfolio
Contact

I have included a link to our Instagram so you get a feel as to how we want to be.

We want to be approachable to new and rural businesses. - Colours included as image

Target Market(s)

Start Up Businesses & Rural Businesses

Number of Pages Required

2 page

Font styles to use
Serif
Other font styles liked:
• Barnyard, Rustic

Requirements
Must have
• Menu, Social Media Icons, rustic lines like our social media.

```html
<!DOCTYPE html>
<html lang="en">
<head>
<meta charset="utf-8">
<title>Copperwick Marketing Agency</title>
<link rel="stylesheet" href="https://fonts.googleapis.com/css2?family=IM+Fell+English+SC&family=Alike&family=Sacramento&display=swap">
<style>
:root{
  --green:#10524a;
  --green-deep:#0c453e;
  --maroon:#7a1f3d;
  --yellow:#f8cd22;
  --beige:#efe9d6;
  --cream:#fcf8ed;
  --ink:#3c3a34;
  --white:#ffffff;
}
*{box-sizing:border-box;margin:0;padding:0}
html,body{width:1200px;height:4898px;overflow:hidden}
body{position:relative;background:var(--cream);font-family:"Alike",serif;color:var(--ink)}
.abs{position:absolute}
.head-font{font-family:"IM Fell English SC",serif}
.script{font-family:"Sacramento",cursive;font-weight:400}

/* header */
.site-header{position:absolute;left:0;top:0;width:1200px;height:176px;background:var(--green)}
.brand{position:absolute;left:42px;top:50px;display:flex;align-items:center;gap:14px;color:var(--white);font-family:"IM Fell English SC",serif;font-size:44px;line-height:1}
.brand-dot{width:22px;height:22px;border-radius:50%;background:var(--yellow)}
.call{position:absolute;left:598px;top:34px;display:flex;align-items:center;gap:10px;color:var(--white);font-family:"IM Fell English SC",serif;font-size:27px}
.call b{color:var(--yellow);font-weight:400}
.btn{display:flex;align-items:center;justify-content:center;background:var(--yellow);color:var(--green);font-family:"IM Fell English SC",serif;text-transform:uppercase;clip-path:polygon(1% 8%,20% 0,45% 6%,70% 1%,99% 5%,100% 50%,98% 96%,72% 100%,44% 94%,18% 100%,0 95%,2% 50%)}
.btn-header{position:absolute;left:926px;top:24px;width:234px;height:58px;font-size:22px}
.main-nav{position:absolute;left:258px;top:112px;width:912px;display:flex;justify-content:space-between;font-family:"IM Fell English SC",serif;font-size:15px;color:var(--white);text-transform:uppercase}

/* hero */
.hero{position:absolute;left:0;top:176px;width:1200px;height:662px;background:radial-gradient(ellipse at 50% 45%,#b88a5a 0%,#8c6a4a 35%,#5b5048 70%,#3d3a38 100%)}
.hero-title{position:absolute;left:0;top:410px;width:1200px;text-align:center;color:var(--white);font-family:"IM Fell English SC",serif;font-size:130px;line-height:1;text-shadow:0 3px 10px rgba(0,0,0,.35)}
.btn-hero{position:absolute;left:481px;top:628px;width:236px;height:60px;font-size:22px}

.tear{position:absolute;left:0;width:1200px;height:28px}

/* services */
.services{position:absolute;left:0;top:836px;width:1200px;height:876px;background:var(--beige)}
.section-title{position:absolute;left:0;width:1200px;text-align:center}
.section-title .script{display:block;color:var(--maroon);font-size:78px;line-height:1;margin-left:120px}
.section-title .head-font{display:block;color:var(--green);font-size:80px;line-height:1;margin-top:-6px;letter-spacing:2px}
.diamond{position:absolute;width:310px;height:310px}
.diamond svg.shape{position:absolute;inset:0}
.diamond-body{position:absolute;left:55px;top:62px;width:200px;text-align:center;color:var(--yellow)}
.diamond-body svg{display:block;margin:0 auto 6px}
.diamond-body h3{font-family:"IM Fell English SC",serif;font-weight:400;font-size:27px;line-height:1}
.diamond-body p{font-family:"Sacramento",cursive;font-size:17px;color:var(--white);line-height:1.2;margin-top:6px}

/* about */
.about-title{position:absolute;left:129px;top:1810px}
.about-title .small{font-family:"IM Fell English SC",serif;font-size:31px;color:var(--green)}
.about-title .script{font-size:80px;color:var(--maroon);margin-left:10px}
.about-title .big{display:block;font-family:"IM Fell English SC",serif;font-size:80px;color:var(--green);line-height:1;margin:-10px 0 0 70px}
.about-copy{position:absolute;left:129px;top:2020px;width:370px;font-size:20px;line-height:30.5px;color:#4a4740}
.photo{position:absolute;background:var(--white);padding:16px;box-shadow:0 6px 16px rgba(0,0,0,.12)}
.photo div{width:100%;height:100%}

/* testimonial */
.testimonial{position:absolute;left:0;top:2568px;width:1200px;height:562px;background:var(--green)}
.brush{position:absolute;left:67px;top:2692px;width:640px;height:312px}
.quote{position:absolute;left:128px;top:2748px;width:460px;color:var(--green)}
.quote p{font-family:"Alike",serif;font-style:italic;font-weight:700;font-size:27px;line-height:31px;padding-left:54px}
.quote .mark{position:absolute;font-family:Georgia,serif;font-size:70px;line-height:1;color:#b99a3a}
.quote cite{display:block;font-style:normal;font-family:"IM Fell English SC",serif;font-size:27px;margin:18px 0 0 54px}
.ring{position:absolute;left:728px;top:2680px;width:330px;height:330px}

/* portfolio */
.portfolio-intro{position:absolute;left:200px;top:3372px;width:800px;text-align:center;font-size:20px;line-height:30px;color:#4a4740}
.frame{position:absolute;padding:34px}
.frame.m{background:var(--maroon)}
.frame.g{background:var(--green)}
.frame div{width:100%;height:100%}
.btn-load{position:absolute;left:479px;top:4181px;width:236px;height:60px;font-size:22px}

/* footer */
.site-footer{position:absolute;left:0;top:4356px;width:1200px;height:542px;background:var(--green);color:var(--white)}
.foot-h{position:absolute;font-family:"IM Fell English SC",serif;font-size:32px;color:var(--yellow);font-weight:400}
.info{position:absolute;left:126px;display:flex;gap:14px;align-items:flex-start;font-size:15px;line-height:20px}
.info .icon{flex:none;width:40px;height:40px;border-radius:50%;background:var(--yellow);display:flex;align-items:center;justify-content:center}
.info b{display:block;color:var(--yellow);font-weight:400;font-size:22px;line-height:26px}
.field{position:absolute;border:2px solid var(--yellow);color:var(--white);font-size:14px;padding:10px 12px}
.btn-submit{position:absolute;left:519px;top:4784px;width:160px;height:56px;font-size:24px}
.foot-brand{position:absolute;left:842px;top:4528px;display:flex;align-items:center;gap:14px;font-family:"IM Fell English SC",serif;font-size:50px;color:var(--white)}
.social{position:absolute;left:848px;top:4669px;display:flex;gap:12px}
.social span{width:38px;height:38px;border-radius:50%;border:3px solid var(--yellow)}
.copyright{position:absolute;left:848px;top:4762px;font-size:16px;line-height:24px}
</style>
</head>
<body>

<svg width="0" height="0" style="position:absolute" aria-hidden="true">
  <defs>
    <pattern id="tear-beige" width="48" height="28" patternUnits="userSpaceOnUse"><path d="M0 28V14L4 9L8 15L12 6L17 12L21 8L25 16L29 7L33 13L38 8L42 15L46 10L48 14V28Z" fill="#efe9d6"/></pattern>
    <pattern id="tear-cream" width="48" height="28" patternUnits="userSpaceOnUse"><path d="M0 28V14L4 9L8 15L12 6L17 12L21 8L25 16L29 7L33 13L38 8L42 15L46 10L48 14V28Z" fill="#fcf8ed"/></pattern>
    <pattern id="tear-green" width="48" height="28" patternUnits="userSpaceOnUse"><path d="M0 28V14L4 9L8 15L12 6L17 12L21 8L25 16L29 7L33 13L38 8L42 15L46 10L48 14V28Z" fill="#10524a"/></pattern>
    <symbol id="rough-diamond" viewBox="0 0 310 310"><path d="M155 4L178 30L192 28L214 60L238 78L252 100L282 128L306 155L284 176L270 190L250 214L230 232L210 258L180 278L155 306L130 284L114 270L92 248L70 228L52 206L24 180L4 155L28 134L46 112L68 90L90 70L110 52L132 28Z"/></symbol>
  </defs>
</svg>

<header class="site-header">
  <div class="brand"><span class="brand-dot"></span>Copperwick</div>
  <div class="call">
    <svg width="34" height="34" viewBox="0 0 34 34" aria-hidden="true"><circle cx="17" cy="17" r="17" fill="#f8cd22"/><path d="M11 9c1-1 2-1 3 0l2 3c.5 1 .3 2-.5 2.6l-1 .8c.8 2 2.3 3.6 4.2 4.5l.9-1c.7-.8 1.7-1 2.6-.4l3 2c1 .7 1 2 0 3l-1.4 1.4C21 27 8 15 11 9Z" fill="#10524a"/></svg>
    CALL US: <b>555 014 2290</b>
  </div>
  <a class="btn btn-header">Get started here</a>
  <nav class="main-nav">
    <span>Home</span><span>About</span><span>Design</span><span>Websites</span><span>Social Media</span><span>Managed Marketing</span><span>Portfolio</span><span>Contact</span>
  </nav>
</header>

<section class="hero" role="img" aria-label="Overhead photo of a team meeting around a wooden table with laptops and papers"></section>
<h1 class="hero-title">Copperwick</h1>
<a class="btn btn-hero">Get started here</a>

<section class="services">
  <h2 class="section-title" style="top:84px"><span class="script">Our</span><span class="head-font">SERVICES</span></h2>

  <div class="diamond" style="left:124px;top:256px">
    <svg class="shape" width="310" height="310" fill="#10524a"><use href="#rough-diamond"/></svg>
    <div class="diamond-body">
      <svg width="50" height="50" viewBox="0 0 50 50" fill="none" stroke="#f8cd22" stroke-width="3" aria-hidden="true"><path d="M25 8L36 28L25 44L14 28Z"/><circle cx="25" cy="28" r="3"/><path d="M6 8H44M25 4V12"/></svg>
      <h3>DESIGN</h3><p>Sed ut perspiciatis unde omnis iste natus</p>
    </div>
  </div>

  <div class="diamond" style="left:446px;top:256px">
    <svg class="shape" width="310" height="310" fill="#7a1f3d"><use href="#rough-diamond"/></svg>
    <div class="diamond-body">
      <svg width="50" height="50" viewBox="0 0 50 50" fill="none" stroke="#f8cd22" stroke-width="3" aria-hidden="true"><rect x="5" y="8" width="40" height="28" rx="2"/><path d="M18 44H32M25 36V44M11 16H30M11 22H38M11 28H24"/></svg>
      <h3>WEBSITES</h3><p>Sed ut perspiciatis unde omnis iste natus</p>
    </div>
  </div>

  <div class="diamond" style="left:766px;top:256px">
    <svg class="shape" width="310" height="310" fill="#10524a"><use href="#rough-diamond"/></svg>
    <div class="diamond-body">
      <svg width="50" height="50" viewBox="0 0 50 50" fill="none" stroke="#f8cd22" stroke-width="3" aria-hidden="true"><rect x="6" y="12" width="32" height="32" rx="2"/><path d="M20 34L24 24L42 6L46 10L28 28Z"/><path d="M12 22H22M12 30H16"/></svg>
      <h3>SOCIAL MEDIA</h3><p>Sed ut perspiciatis unde omnis iste natus</p>
    </div>
  </div>

  <div class="diamond" style="left:280px;top:464px">
    <svg class="shape" width="310" height="310" fill="#7a1f3d"><use href="#rough-diamond"/></svg>
    <div class="diamond-body">
      <svg width="50" height="50" viewBox="0 0 50 50" aria-hidden="true"><path d="M27 6C14 6 6 15 6 26s8 18 16 18c4 0 4-4 2-6s0-5 4-5h6c6 0 10-4 10-10C44 13 37 6 27 6Z" fill="#f8cd22"/><circle cx="16" cy="22" r="3" fill="#7a1f3d"/><circle cx="24" cy="14" r="3" fill="#7a1f3d"/><circle cx="34" cy="17" r="3" fill="#7a1f3d"/></svg>
      <h3>GRAPHIC<br>DESIGN</h3><p>Sed ut perspiciatis unde</p>
    </div>
  </div>

  <div class="diamond" style="left:612px;top:464px">
    <svg class="shape" width="310" height="310" fill="#7a1f3d"><use href="#rough-diamond"/></svg>
    <div class="diamond-body">
      <svg width="50" height="50" viewBox="0 0 50 50" aria-hidden="true"><circle cx="25" cy="25" r="18" fill="#f8cd22"/><circle cx="25" cy="25" r="7" fill="#7a1f3d"/><path d="M25 2V10M25 40V48M2 25H10M40 25H48M9 9L14 14M36 36L41 41M41 9L36 14M14 36L9 41" stroke="#f8cd22" stroke-width="5"/></svg>
      <h3>MANAGED<br>MARKETING</h3><p>Sed ut perspiciatis unde</p>
    </div>
  </div>
</section>
<svg class="tear" style="top:812px" aria-hidden="true"><rect width="1200" height="28" fill="url(#tear-beige)"/></svg>
<svg class="tear" style="top:1690px" aria-hidden="true"><rect width="1200" height="28" fill="url(#tear-cream)"/></svg>

<section class="about">
  <h2 class="about-title"><span class="small">ABOUT</span><span class="script">Copperwick</span><span class="big">AGENCY</span></h2>
  <p class="about-copy">Sed ut perspiciatis unde omnis iste natus error sit voluptatem accusanum doloremque laudantium, totam lorerem aperiam, eaque ipsa quae ablore,lorillo inventore veritatis et quasi architecto beatae vitae dicta sunt explicabo.emo enim ipsam voluptatem quia voluptas sit aspernatur aut odit aut fugit, sed quia consequuntur magni dolores eos qui ratione voluptatem sequi nesciunt. Neque porro quisquam est, qui dolrem ipsum quia dolor sit amet, consectetr, adipisci velit, sed.</p>
  <div class="photo" style="left:732px;top:1860px;width:380px;height:350px;transform:rotate(2deg)"><div role="img" aria-label="Photo of two colleagues working together in an office" style="background:linear-gradient(135deg,#5a5e63,#9a8f86 55%,#d8d2cb)"></div></div>
  <div class="photo" style="left:570px;top:2030px;width:370px;height:370px;transform:rotate(-6deg)"><div role="img" aria-label="Photo of two women reviewing work at a desk" style="background:linear-gradient(135deg,#d9d3c7,#b88a52 45%,#5a2a2a)"></div></div>
</section>

<section class="testimonial" role="img" aria-label="Faint photo of a team at work, tinted green"></section>
<svg class="tear" style="top:2546px" aria-hidden="true"><rect width="1200" height="28" fill="url(#tear-green)"/></svg>
<svg class="brush" viewBox="0 0 640 312" aria-hidden="true"><path d="M18 40L60 26L120 34L200 18L280 28L360 14L440 26L520 12L600 30L630 70L612 120L636 170L610 220L624 270L570 296L480 284L400 300L300 286L200 302L120 288L40 298L10 250L28 200L6 150L24 100Z" fill="#f8cd22"/></svg>
<blockquote class="quote">
  <span class="mark" style="left:0;top:6px">&#8220;</span>
  <p>Sed ut perspiciatis unde omnis iste natus error sit voluptatem accusantiudrebfm dolorem <span style="font-family:Georgia,serif;color:#b99a3a;font-style:normal">&#8221;</span></p>
  <cite>DELLA HART</cite>
</blockquote>
<svg class="ring" viewBox="0 0 330 330" aria-hidden="true"><circle cx="165" cy="165" r="158" fill="none" stroke="#e7efe9" stroke-width="5" stroke-dasharray="60 8 30 6"/></svg>
<div class="abs" role="img" aria-label="Photo of two colleagues smiling at a laptop" style="left:746px;top:2698px;width:294px;height:294px;border-radius:50%;background:linear-gradient(135deg,#e9e6e0,#b7b2ad 50%,#6d6663)"></div>
<svg class="tear" style="top:3108px" aria-hidden="true"><rect width="1200" height="28" fill="url(#tear-cream)"/></svg>

<section class="portfolio">
  <h2 class="section-title" style="top:3176px"><span class="script">Our</span><span class="head-font">PORTFOLIO</span></h2>
  <p class="portfolio-intro">Sed ut perspiciatis unde omnis iste natus error sit voluptatem accusantium doloremque laudantium, totam lorerem aperiam, eaque ipsa quae ablor.</p>
  <div class="frame m" style="left:91px;top:3481px;width:318px;height:304px"><div role="img" aria-label="Photo of hands on a tablet and laptop" style="background:linear-gradient(135deg,#6f5c4c,#c8c0b4 55%,#efece6)"></div></div>
  <div class="frame g" style="left:437px;top:3481px;width:662px;height:304px"><div role="img" aria-label="Photo of a person at a desk with a phone and plant" style="background:linear-gradient(90deg,#e7e6e1,#c9c3b8 50%,#b07a4c)"></div></div>
  <div class="frame g" style="left:91px;top:3823px;width:318px;height:304px"><div role="img" aria-label="Photo of hands writing on a document" style="background:linear-gradient(135deg,#3b4247,#7a7775 55%,#a59483)"></div></div>
  <div class="frame m" style="left:437px;top:3823px;width:316px;height:304px"><div role="img" aria-label="Photo of colleagues talking at a laptop" style="background:linear-gradient(135deg,#cfc7bc,#8e7461 55%,#4d3c33)"></div></div>
  <div class="frame g" style="left:782px;top:3823px;width:317px;height:304px"><div role="img" aria-label="Photo of business people reviewing a folder" style="background:linear-gradient(135deg,#dcd8d2,#6e7483 55%,#2e3140)"></div></div>
  <a class="btn btn-load">Load more</a>
</section>
<svg class="tear" style="top:4334px" aria-hidden="true"><rect width="1200" height="28" fill="url(#tear-green)"/></svg>

<footer class="site-footer">
  <h3 class="foot-h" style="left:127px;top:134px">LOCATION</h3>
  <div class="info" style="top:216px">
    <span class="icon"><svg width="20" height="24" viewBox="0 0 20 24" aria-hidden="true"><path d="M10 0C4.5 0 1 4 1 8.6 1 14 10 24 10 24S19 14 19 8.6C19 4 15.5 0 10 0Z" fill="#10524a"/><circle cx="10" cy="8.5" r="3.4" fill="#f8cd22"/></svg></span>
    <span>Company name line56<br>lorem ipshm street 67 lore<br>slorhart 56747<br>Loremm 93jj doeHGT</span>
  </div>
  <div class="info" style="top:328px">
    <span class="icon"><svg width="22" height="22" viewBox="10 8 18 19" aria-hidden="true"><path d="M11 9c1-1 2-1 3 0l2 3c.5 1 .3 2-.5 2.6l-1 .8c.8 2 2.3 3.6 4.2 4.5l.9-1c.7-.8 1.7-1 2.6-.4l3 2c1 .7 1 2 0 3l-1.4 1.4C21 27 8 15 11 9Z" fill="#10524a"/></svg></span>
    <span>Phone:<b>555 018 4471</b></span>
  </div>
  <div class="info" style="top:396px">
    <span class="icon"><svg width="22" height="16" viewBox="0 0 22 16" aria-hidden="true"><rect width="22" height="16" rx="2" fill="#10524a"/><path d="M1 2L11 9L21 2" fill="none" stroke="#f8cd22" stroke-width="2"/></svg></span>
    <span>Email:<br>hello@copperwick.co</span>
  </div>

  <h3 class="foot-h" style="left:527px;top:134px">CONTACT</h3>
  <div class="field" style="left:428px;top:209px;width:181px;height:48px">Name</div>
  <div class="field" style="left:622px;top:209px;width:150px;height:48px">Phone</div>
  <div class="field" style="left:428px;top:275px;width:344px;height:54px">Email</div>
  <div class="field" style="left:428px;top:338px;width:344px;height:120px">Message</div>
  <a class="btn btn-submit" style="top:428px">Submit</a>

  <div class="foot-brand" style="top:172px"><span class="brand-dot"></span>Copperwick</div>
  <div class="social" style="top:313px" aria-label="Social media links"><span></span><span></span><span></span><span></span></div>
  <p class="copyright" style="top:406px">© 2021 Copperwick Marketing.<br>All Rights Reserved</p>
</footer>

</body>
</html>
```